"Autumn Special" 6 Month Membership Special

Running a Membership Drive on a 6 month membership option for the month of April/May. 6 months $150.00 save 50%. Below is recent ads made from designers on Vellum Forge to assist. Final design should be inviting / colorful and eye catching

Format required is for a Facebook cover, Instagram, and A0 format for a poster .

Target Market(s)

16-40 male and female

Industry/Entity Type

Fitness

Font styles to use
Serif
Other font styles liked:
• Athletic

Colors

Designer to choose colors to be used in the design.

Requirements
Must have
• The main emphasis would be on the "6 MONTH SPECIAL" or "AUTUMN SPECIAL" font/text (special) and the layout of the text. If we can add some brighter colors to the layout that would be great just to capture their attention. If there's any effects you want to add to it that would be great. The logo can be faint in the background. The image of the female model can some some artistic effects around it and she does not have to be the main focus
• "AUTUMN SPECIAL"
• 6 MONTHS from
• $150.00
• SAVE 50%"
• "Terms and conditions apply"
• All contact details, address, website, etc which will be supplied
Nice to have
• Some artistic effects to catch your eye and enhance the professionalism of the designer. Attached is a "Athletic font" Logo which that style could be incorporated
Should not have
• You don't have to include the orange background of the female model, you can use her silhouette

```html
<!DOCTYPE html>
<html lang="en">
<head>
<meta charset="utf-8">
<title>Summit Gymnasium — Autumn Special</title>
<link href="https://fonts.googleapis.com/css2?family=Montserrat:wght@800;900&family=Titillium+Web:wght@700&family=Source+Sans+3:wght@600;700&family=Passion+One:wght@700&display=swap" rel="stylesheet">
<style>
  :root{
    --board-light:#8c8c8c;
    --board-dark:#2e2e30;
    --paper:#f4f4f4;
    --paper-edge:#d6d6d6;
    --magenta:#ec0f5c;
    --purple:#9b3df2;
    --purple-deep:#6a1fc0;
    --ink-purple:#2b1446;
    --yellow:#ffe000;
    --cyan:#1fb8c4;
    --ink:#111111;
    --white:#ffffff;
    --athlete-top:#5d6f8f;
    --athlete-low:#8fa0bd;
  }
  *{margin:0;padding:0;box-sizing:border-box}
  html,body{width:1200px;height:843px;overflow:hidden}
  body{
    position:relative;
    background:radial-gradient(ellipse at 25% 15%,var(--board-light) 0%,#5e5e60 45%,var(--board-dark) 100%);
    font-family:"Source Sans 3",sans-serif;
  }
  .ad{
    position:absolute;overflow:hidden;
    background:radial-gradient(circle at 55% 40%,var(--white) 0%,var(--paper) 45%,var(--paper-edge) 100%);
    box-shadow:0 8px 22px rgba(0,0,0,.45);
  }
  .ad--cover{left:36px;top:60px;width:604px;height:282px}
  .ad--square{left:104px;top:362px;width:413px;height:406px}
  .ad--poster{left:658px;top:58px;width:502px;height:709px}
  .ad svg.shapes{position:absolute;inset:0;width:100%;height:100%}

  .brand{
    position:absolute;display:flex;align-items:center;justify-content:center;gap:.35em;
    font-family:"Source Sans 3",sans-serif;font-weight:700;color:var(--ink);white-space:nowrap;line-height:1;
  }
  .brand__mark{display:inline-block;width:.8em;height:.8em;background:var(--ink)}

  .headline{
    position:absolute;white-space:nowrap;
    font-family:"Passion One",sans-serif;font-weight:700;
    color:var(--purple);
    -webkit-text-stroke:1.2px var(--ink-purple);
    text-shadow:2px 2px 0 var(--ink-purple),3px 3px 0 var(--ink-purple);
    transform:rotate(-5deg) skewX(-12deg);transform-origin:left bottom;
  }
  .offer{position:absolute;font-family:"Montserrat",sans-serif;font-weight:900;color:var(--white);line-height:.92;
    text-shadow:2px 2px 0 #2a1030,3px 3px 2px rgba(0,0,0,.5);transform:rotate(-4deg);transform-origin:left top;white-space:nowrap}
  .offer span{display:block}
  .save{position:absolute;font-family:"Titillium Web",sans-serif;font-weight:700;white-space:nowrap;
    color:#e7e0f2;text-shadow:1px 2px 2px rgba(40,10,70,.6);transform:rotate(-3deg)}
  .terms{position:absolute;font-family:"Montserrat",sans-serif;font-weight:800;color:#333;white-space:nowrap;letter-spacing:.04em}
  .athlete{position:absolute;border-radius:45% 40% 30% 30%;
    background:linear-gradient(170deg,var(--athlete-top),var(--athlete-low) 70%,rgba(143,160,189,0));
    opacity:.85}
  .contact{position:absolute;font-weight:700;color:var(--ink);line-height:1.25;white-space:nowrap}
  .contact .web{display:block}
  .contact--accent .web{color:var(--purple)}
</style>
</head>
<body>

<section class="ad ad--cover" aria-label="Facebook cover">
  <svg class="shapes" viewBox="0 0 604 282" aria-hidden="true">
    <polygon points="60,195 100,230 290,252 260,212" fill="var(--yellow)"/>
    <polygon points="58,45 250,36 262,225 70,215" fill="none" stroke="var(--cyan)" stroke-width="3" transform="rotate(-4 160 130)"/>
    <polygon points="140,38 290,18 180,17" fill="var(--purple)"/>
    <polygon points="10,50 355,30 330,212 88,228" fill="var(--magenta)"/>
    <polygon points="28,112 55,158 30,150" fill="var(--purple)"/>
    <polygon points="402,122 594,122 574,172 410,172" fill="var(--purple-deep)" transform="translate(4,6)"/>
    <polygon points="402,122 594,122 574,172 410,172" fill="var(--purple)"/>
  </svg>
  <div class="athlete" style="left:300px;top:36px;width:100px;height:232px" role="img" aria-label="Photo of a female athlete sprinting with dumbbells"></div>
  <div class="headline" style="left:44px;top:48px;font-size:36px">AUTUMN SPECIAL</div>
  <div class="offer" style="left:128px;top:98px">
    <span style="font-size:22px">6 MONTHS</span>
    <span style="font-size:40px">FROM</span>
    <span style="font-size:36px">$150.00</span>
  </div>
  <div class="save" style="left:430px;top:126px;font-size:29px">SAVE 50%</div>
  <div class="terms" style="left:440px;top:178px;font-size:5px">*TERMS AND CONDITIONS APPLY</div>
  <div class="brand" style="left:400px;top:40px;width:180px;font-size:20px"><span class="brand__mark"></span>Summit Gymnasium</div>
  <div class="contact" style="right:32px;top:240px;text-align:center;font-size:9.5px">
    14 Harbour Lane, Northgate Victoria 3099<br>hello@summitgym.com.au<span class="web">www.summitgym.com.au</span>
  </div>
</section>

<section class="ad ad--square" aria-label="Instagram post">
  <svg class="shapes" viewBox="0 0 413 406" aria-hidden="true">
    <polygon points="60,300 100,330 300,345 270,300" fill="var(--yellow)"/>
    <polygon points="70,145 270,130 290,330 70,320" fill="none" stroke="var(--cyan)" stroke-width="3" transform="rotate(-4 180 230)"/>
    <polygon points="150,126 300,102 200,100" fill="var(--purple)"/>
    <polygon points="6,136 352,115 330,288 55,318" fill="var(--magenta)"/>
    <polygon points="26,210 52,254 28,246" fill="var(--purple)"/>
    <polygon points="12,286 204,286 188,332 24,332" fill="var(--purple-deep)" transform="translate(3,5)"/>
    <polygon points="12,286 204,286 188,332 24,332" fill="var(--purple)"/>
  </svg>
  <div class="athlete" style="left:296px;top:118px;width:100px;height:226px" role="img" aria-label="Photo of a female athlete sprinting with dumbbells"></div>
  <div class="headline" style="left:34px;top:132px;font-size:36px">AUTUMN SPECIAL</div>
  <div class="offer" style="left:116px;top:182px">
    <span style="font-size:22px">6 MONTHS</span>
    <span style="font-size:40px">FROM</span>
    <span style="font-size:36px">$150.00</span>
  </div>
  <div class="save" style="left:40px;top:288px;font-size:30px">SAVE 50%</div>
  <div class="terms" style="left:52px;top:338px;font-size:5px">*TERMS AND CONDITIONS APPLY</div>
  <div class="brand" style="left:0;top:40px;width:413px;font-size:24px"><span class="brand__mark"></span>Summit Gymnasium</div>
  <div class="contact" style="left:0;width:413px;top:366px;text-align:center;font-size:10.5px">
    14 Harbour Lane, Northgate Victoria 3099<br>hello@summitgym.com.au<span class="web">www.summitgym.com.au</span>
  </div>
</section>

<section class="ad ad--poster" aria-label="A0 poster">
  <svg class="shapes" viewBox="0 0 502 709" aria-hidden="true">
    <polygon points="60,168 215,150 230,180 62,196" fill="var(--yellow)"/>
    <polygon points="380,218 474,222 420,330" fill="var(--yellow)"/>
    <polygon points="108,176 370,150 380,200" fill="none" stroke="var(--cyan)" stroke-width="3"/>
    <polygon points="170,176 340,150 225,145" fill="var(--purple)"/>
    <polygon points="2,200 420,146 406,422 26,432" fill="var(--magenta)"/>
    <polygon points="36,268 68,318 38,312" fill="var(--purple)"/>
    <polygon points="20,442 326,426 302,520 38,520" fill="var(--purple-deep)" transform="translate(6,8)"/>
    <polygon points="20,438 326,422 302,514 38,514" fill="var(--purple)"/>
    <polygon points="180,580 265,570 180,590" fill="var(--purple)"/>
    <polygon points="230,590 270,575 240,600" fill="var(--purple)"/>
    <polygon points="228,382 262,372 232,392" fill="var(--white)"/>
  </svg>
  <div class="athlete" style="left:332px;top:206px;width:150px;height:392px" role="img" aria-label="Photo of a female athlete sprinting with dumbbells"></div>
  <div class="headline" style="left:48px;top:196px;font-size:54px;transform:rotate(-7deg) skewX(-12deg)">AUTUMN SPECIAL</div>
  <div class="offer" style="left:118px;top:256px">
    <span style="font-size:33px">6 MONTHS</span>
    <span style="font-size:58px">FROM</span>
    <span style="font-size:50px">$150.00</span>
  </div>
  <div class="save" style="left:60px;top:438px;font-size:50px">SAVE 50%</div>
  <div class="terms" style="left:114px;top:516px;font-size:8.5px">*TERMS AND CONDITIONS APPLY</div>
  <div class="brand" style="left:0;top:56px;width:502px;font-size:38px"><span class="brand__mark"></span>Summit Gymnasium</div>
  <div class="contact contact--accent" style="left:0;width:502px;top:640px;text-align:center;font-size:14.5px">
    14 Harbour Lane, Northgate Victoria 3099<br>hello@summitgym.com.au<span class="web">www.summitgym.com.au</span>
  </div>
</section>

</body>
</html>
```